Business card design with slight adjustment to current logo
Marlow Heating Cooling & Plumbing
Business card design with slight adjustment to current logo - Trade
Creative Brief
Bright & Fun-filled
no name wanted on card
no title wanted on card
3167 Penwick Ave Findlay, OH 45893
marlowhvacfindlay@examplemail.test
marlow-hvac.test
Heating Cooling Plumbing The logo I have is an older logo, we want to keep it the same but the type of file I have it flat looking, plain colored. If the logo can be tweaked to look brighter, less flat, but very similar so as not to look much different I would appreciate that. My hope was to have the flame in the logo look a little more like a flame, I think maybe the curve of it is just a little off, making it more like a shark fin or something. for the logo and business card, that color blue in logo is a favorite.
Tkvorel42 Tkvorel42
Cards can also say: Service & Install Free Estimates
This is more me looking for business card designs, if the logo can be adjusted a little bit and you have the idea for it, fine. But mainly I need good business card designs for current logo

```html
<!DOCTYPE html>
<html lang="en">
<head>
<meta charset="utf-8">
<title>Marlow Heating Cooling &amp; Plumbing — Business Card</title>
<link rel="stylesheet" href="https://fonts.googleapis.com/css2?family=Montserrat:wght@400;500;800&display=swap">
<style>
  :root {
    --backdrop: #e4e4e4;
    --card-white: #ffffff;
    --ink: #1a1a1a;
    --ink-soft: #3a3a3a;
    --brand-blue: #1a8fd6;
    --brand-blue-deep: #0b5f9c;
    --card-black: #141414;
    --card-black-soft: #262626;
  }
  * { box-sizing: border-box; margin: 0; padding: 0; }
  html, body { width: 1200px; height: 802px; overflow: hidden; }
  body {
    background: var(--backdrop);
    font-family: "Montserrat", sans-serif;
    color: var(--ink);
    position: relative;
  }
  .card {
    position: absolute;
    top: 246px;
    width: 540px;
    height: 310px;
    border-radius: 4px;
    overflow: hidden;
    box-shadow: 0 6px 18px rgba(0,0,0,0.18);
  }
  .card-front { left: 40px; background: var(--card-white); }
  .card-back { left: 620px; background: var(--card-black); }

  .front-swoosh { position: absolute; inset: 0; width: 100%; height: 100%; }

  .brand {
    position: absolute;
    left: 40px;
    top: 52px;
    display: flex;
    align-items: center;
    gap: 12px;
  }
  .brand-dot {
    width: 26px; height: 26px;
    border-radius: 50%;
    background: var(--brand-blue);
    flex: none;
  }
  .brand-name {
    font-weight: 800;
    font-size: 22px;
    line-height: 1.1;
    color: var(--ink);
    text-transform: uppercase;
    letter-spacing: 0.5px;
  }
  .brand-name .line { display: block; }
  .brand-name .line-small { font-size: 11px; letter-spacing: 1.4px; margin-top: 3px; }

  .address {
    position: absolute;
    left: 40px;
    top: 148px;
    font-size: 12px;
    line-height: 1.5;
    color: var(--ink-soft);
    font-style: normal;
  }
  .contact-list {
    position: absolute;
    left: 40px;
    top: 200px;
    list-style: none;
    font-size: 12px;
    color: var(--ink-soft);
  }
  .contact-item { display: flex; align-items: center; gap: 8px; margin-bottom: 7px; }
  .contact-icon {
    width: 15px; height: 15px;
    border-radius: 50%;
    background: var(--brand-blue);
    display: flex; align-items: center; justify-content: center;
    flex: none;
  }
  .contact-icon svg { width: 9px; height: 9px; }

  .back-pattern {
    position: absolute;
    inset: 0;
    background: radial-gradient(circle at 50% 45%, var(--card-black-soft), var(--card-black) 75%);
  }
</style>
</head>
<body>
  <section class="card card-front" aria-label="Business card front">
    <svg class="front-swoosh" viewBox="0 0 540 310" preserveAspectRatio="none" aria-hidden="true">
      <path d="M540 0 L360 0 C420 70 440 200 420 310 L540 310 Z" fill="var(--card-black)"/>
      <path d="M340 0 C400 70 420 200 398 310 L414 310 C436 200 414 70 354 0 Z" fill="var(--brand-blue)"/>
      <path d="M320 0 C378 70 398 200 378 310 L384 310 C404 200 384 70 326 0 Z" fill="var(--card-black)"/>
    </svg>

    <div class="brand">
      <span class="brand-dot" aria-hidden="true"></span>
      <p class="brand-name">
        <span class="line">Marlow</span>
        <span class="line line-small">Heating Cooling &amp; Plumbing</span>
      </p>
    </div>

    <address class="address">
      3167 Penwick Ave<br>
      Findlay, OH 45893
    </address>

    <ul class="contact-list">
      <li class="contact-item">
        <span class="contact-icon"><svg viewBox="0 0 10 10"><path d="M2 1 L4 1 L4.6 3 L3.4 3.8 C4 5.2 4.8 6 6.2 6.6 L7 5.4 L9 6 L9 8 C5 8.4 1.6 5 2 1 Z" fill="#fff"/></svg></span>
        419-555-0187
      </li>
      <li class="contact-item">
        <span class="contact-icon"><svg viewBox="0 0 10 10"><rect x="1" y="2.5" width="8" height="5" fill="none" stroke="#fff" stroke-width="1"/><path d="M1 2.5 L5 5.5 L9 2.5" fill="none" stroke="#fff" stroke-width="1"/></svg></span>
        marlowhvacfindlay@examplemail.test
      </li>
      <li class="contact-item">
        <span class="contact-icon"><svg viewBox="0 0 10 10"><circle cx="5" cy="5" r="3.6" fill="none" stroke="#fff" stroke-width="0.9"/><path d="M1.4 5 H8.6 M5 1.4 C3.4 3 3.4 7 5 8.6 M5 1.4 C6.6 3 6.6 7 5 8.6" fill="none" stroke="#fff" stroke-width="0.8"/></svg></span>
        www.marlow-hvac.test
      </li>
    </ul>
  </section>

  <section class="card card-back" aria-label="Business card back">
    <div class="back-pattern" role="img" aria-label="Gloss black repeating droplet pattern across the card back"></div>
  </section>
</body>
</html>
```